Larkspur Stillness

Logo picture and I want it to say

yoga. meditation. sound healing

small sweet classes

Larkspur-stillness.com

2740 West Hollander Ave Suite K
Santa Barbara ca 93108

```html
<!DOCTYPE html>
<html lang="en">
<head>
<meta charset="utf-8">
<title>Larkspur Stillness – Small Sweet Classes</title>
<link rel="stylesheet" href="https://fonts.googleapis.com/css2?family=Open+Sans:wght@600;700&family=Marcellus&display=swap">
<style>
  :root {
    --page: #e9e7e4;
    --card: #f4ece8;
    --card-warm: #efe4de;
    --ink: #231f20;
    --ink-soft: #3a3436;
    --violet: #7d4fc9;
    --orchid: #c36fd1;
    --lilac: #d9b3e6;
    --lilac-soft: #ead4ef;
    --photo-light: #efe6e0;
    --photo-mid: #d8c6bb;
    --photo-deep: #8c7a70;
  }
  * { box-sizing: border-box; margin: 0; padding: 0; }
  html, body {
    width: 1200px; height: 800px; overflow: hidden;
    background: var(--page);
  }
  .canvas {
    position: relative; width: 1200px; height: 800px;
    display: flex; align-items: center; justify-content: center;
  }
  .rack-card {
    position: relative; width: 1100px; height: 580px; overflow: hidden;
    background: linear-gradient(90deg, var(--card) 0%, var(--card-warm) 45%, var(--photo-light) 100%);
    box-shadow: 0 10px 30px rgba(0,0,0,0.12);
  }
  .class-photo {
    position: absolute; right: 0; top: 0; width: 640px; height: 100%;
    background:
      radial-gradient(ellipse 70% 55% at 65% 55%, var(--photo-deep) 0%, rgba(140,122,112,0.35) 45%, transparent 75%),
      linear-gradient(180deg, var(--photo-light) 0%, var(--photo-mid) 70%, var(--photo-light) 100%);
    -webkit-mask-image: linear-gradient(90deg, transparent 0%, #000 22%);
            mask-image: linear-gradient(90deg, transparent 0%, #000 22%);
  }
  .ornament {
    position: absolute;
    background: radial-gradient(ellipse at center, var(--lilac) 0%, var(--lilac-soft) 55%, transparent 75%);
    opacity: 0.8;
  }
  .ornament--top { left: 300px; top: -90px; width: 420px; height: 220px; border-radius: 50%; }
  .ornament--bottom { left: -70px; bottom: -70px; width: 360px; height: 190px; border-radius: 50%; }

  .brand {
    position: absolute; left: 70px; top: 90px;
    display: flex; align-items: center; gap: 14px;
  }
  .brand__mark {
    width: 30px; height: 30px; border-radius: 50%;
    border: 3px solid var(--ink-soft);
  }
  .brand__name {
    font-family: "Open Sans", sans-serif; font-weight: 600;
    font-size: 26px; color: var(--ink-soft);
  }
  .offer {
    position: absolute; left: 70px; top: 250px; width: 440px;
  }
  .offer__services {
    font-family: "Open Sans", sans-serif; font-weight: 700;
    font-size: 24px; color: var(--ink); letter-spacing: 0.2px;
  }
  .offer__headline {
    margin-top: 14px;
    font-family: "Marcellus", serif; font-size: 54px; line-height: 1.02;
    text-transform: uppercase; letter-spacing: 1px;
    background: linear-gradient(90deg, var(--orchid) 0%, var(--violet) 100%);
    -webkit-background-clip: text; background-clip: text; color: transparent;
  }
  .offer__address {
    margin-top: 22px;
    font-family: "Open Sans", sans-serif; font-weight: 600;
    font-size: 25px; line-height: 1.3; color: var(--ink); font-style: normal;
  }
  .offer__web {
    margin-top: 26px;
    font-family: "Open Sans", sans-serif; font-weight: 600;
    font-size: 19px; color: var(--ink);
  }
</style>
</head>
<body>
<main class="canvas">
  <article class="rack-card">
    <div class="class-photo" role="img" aria-label="Photo of a row of women meditating cross-legged on yoga mats in a bright studio"></div>
    <div class="ornament ornament--top" role="img" aria-label="Lilac mandala ornament"></div>
    <div class="ornament ornament--bottom" role="img" aria-label="Lilac mandala ornament"></div>

    <header class="brand">
      <span class="brand__mark"></span>
      <span class="brand__name">Larkspur Stillness</span>
    </header>

    <section class="offer">
      <p class="offer__services">Yoga . Meditation . Sound Healing</p>
      <h1 class="offer__headline">Small Sweet<br>Classes</h1>
      <address class="offer__address">2740 West Hollander Ave Suite K<br>Santa Barbara ca 93108</address>
      <p class="offer__web">www.larkspur-stillness.com</p>
    </section>
  </article>
</main>
</body>
</html>
```